Music Festival Business Cards

The Lantern Gathering
Produced by Bramblewood Sound Collective LLC
New music festival in Arkansas.

Target Market(s)

18-35 year olds

Industry/Entity Type

Festival

Contact Information for Business Card

We are a 5-partner team producing a music festival in Arkansas. We need slick business cards, and I want them to be square.

Requirements
Must have
• I NEED THESE TO BE IN SQUARE SIZE - 2x2 or 2.5x2.5... please not regular size.
• I need www.lanternmeet.example as the link to website.

```html
<!DOCTYPE html>
<html lang="en">
<head>
<meta charset="utf-8">
<title>The Lantern Gathering — Business Cards</title>
<link rel="stylesheet" href="https://fonts.googleapis.com/css2?family=Open+Sans:wght@400;700&display=swap">
<style>
  :root {
    --page-bg: #e9e6e1;
    --card-bg: #0a0a0a;
    --card-edge: #1a1a1a;
    --accent: #3fbfc6;
    --ink-light: #f2f2f2;
  }
  * { margin: 0; padding: 0; box-sizing: border-box; }
  html, body { width: 1200px; height: 1200px; overflow: hidden; }
  body {
    background: var(--page-bg);
    font-family: "Open Sans", Arial, sans-serif;
    display: flex;
    align-items: center;
    justify-content: center;
    gap: 44px;
  }
  .card {
    position: relative;
    width: 540px;
    height: 540px;
    background: var(--card-bg);
    box-shadow: 6px 8px 0 var(--card-edge), 0 14px 30px rgba(0,0,0,0.25);
  }
  .brand {
    display: flex;
    align-items: center;
    gap: 16px;
    color: var(--accent);
    font-weight: 700;
    font-size: 30px;
    line-height: 1.25;
    text-transform: uppercase;
    letter-spacing: 0.08em;
  }
  .brand__mark {
    width: 20px;
    height: 20px;
    flex: none;
    background: var(--accent);
  }
  .brand__name { display: block; }
  .card--front {
    display: flex;
    align-items: center;
    justify-content: center;
  }
  .card--back {
    display: flex;
    flex-direction: column;
    justify-content: space-between;
    padding: 56px 56px 60px;
  }
  .contact { color: var(--ink-light); font-size: 17px; line-height: 1.4; padding-left: 36px; }
  .contact__name {
    color: var(--accent);
    font-weight: 700;
    font-size: 26px;
    text-transform: uppercase;
    line-height: 1.15;
  }
  .contact__role { margin-bottom: 18px; }
  .contact__row { display: flex; align-items: flex-start; gap: 12px; }
  .contact__row + .contact__row { margin-top: 3px; }
  .contact__address { margin-bottom: 16px; }
  .contact__icon { width: 16px; height: 16px; flex: none; margin-top: 4px; fill: var(--accent); }
</style>
</head>
<body>
  <section class="card card--front" aria-label="Card front">
    <div class="brand"><span class="brand__mark"></span><span class="brand__name">The Lantern<br>Gathering</span></div>
  </section>

  <section class="card card--back" aria-label="Card back">
    <div class="brand"><span class="brand__mark"></span><span class="brand__name">The Lantern<br>Gathering</span></div>
    <div class="contact">
      <p class="contact__name">Mara Quinlan</p>
      <p class="contact__role">Director</p>
      <div class="contact__row contact__address">
        <svg class="contact__icon" viewBox="0 0 24 24"><path d="M12 2a7 7 0 0 0-7 7c0 5 7 13 7 13s7-8 7-13a7 7 0 0 0-7-7zm0 9.5A2.5 2.5 0 1 1 12 6.5a2.5 2.5 0 0 1 0 5z"/></svg>
        <p>Hollow Creek<br>Arkansas, United States</p>
      </div>
      <div class="contact__row">
        <svg class="contact__icon" viewBox="0 0 24 24"><path d="M6.6 10.8a15 15 0 0 0 6.6 6.6l2.2-2.2a1 1 0 0 1 1-.25 11.4 11.4 0 0 0 3.6.57 1 1 0 0 1 1 1V20a1 1 0 0 1-1 1A17 17 0 0 1 3 4a1 1 0 0 1 1-1h3.5a1 1 0 0 1 1 1c0 1.25.2 2.45.57 3.6a1 1 0 0 1-.25 1z"/></svg>
        <p>1-555-014-2290</p>
      </div>
      <div class="contact__row">
        <svg class="contact__icon" viewBox="0 0 24 24"><path d="M12 2a10 10 0 1 0 0 20 10 10 0 0 0 0-20zm6.9 6h-3a15.6 15.6 0 0 0-1.4-3.6A8 8 0 0 1 18.9 8zM12 4c.8 1.2 1.5 2.5 1.9 4h-3.8c.4-1.5 1.1-2.8 1.9-4zM4.3 14a8 8 0 0 1 0-4h3.4a16 16 0 0 0 0 4zm.8 2h3a15.6 15.6 0 0 0 1.4 3.6A8 8 0 0 1 5.1 16zm3-8h-3a8 8 0 0 1 4.4-3.6A15.6 15.6 0 0 0 8.1 8zM12 20c-.8-1.2-1.5-2.5-1.9-4h3.8c-.4 1.5-1.1 2.8-1.9 4zm2.3-6H9.7a14.7 14.7 0 0 1 0-4h4.6a14.7 14.7 0 0 1 0 4zm.2 5.6a15.6 15.6 0 0 0 1.4-3.6h3a8 8 0 0 1-4.4 3.6zm1.8-5.6a16 16 0 0 0 0-4h3.4a8 8 0 0 1 0 4z"/></svg>
        <p>www.lanternmeet.example</p>
      </div>
      <div class="contact__row">
        <svg class="contact__icon" viewBox="0 0 24 24"><path d="M2 5h20v14H2zm2 2v.5l8 5 8-5V7zm0 2.9V17h16V9.9l-8 5z"/></svg>
        <p>mara@lanternmeet.example</p>
      </div>
    </div>
  </section>
</body>
</html>
```